Granite Haulers Guild

This piece is to drive tow companies and drivers to join the largest towing association within the state of Texas. It will be 3 pieces. A cover sheet that is mostly graphic with minimal copy, page two will be a letter and is not required for this exercise, page three will be a list of membership benefits and the pricing for each level. I have attached copy and their current logo. However, I DO NOT WANT the logo to drive the design. We need outside of the box thinking that is not confined to the limitations the logo presents.

Target Market(s)

Tow truck companies and drivers. Male 20 to 60 years old.

Industry/Entity Type

Pricing

Requirements
Must have
• The cover sheet must say "Let's Pick Each Other Up" the rest is all graphic and up to your discretion.

Would prefer a Southwestern/Texas type of feel. Down home. Family oriented. We're in this together type of flavor.

Must boldly promote price levels and options for signing up on page three.

Must use the attached copy for page three.
Should not have
• Clipart, Illustrations, ugliness

```html
<!DOCTYPE html>
<html lang="en">
<head>
<meta charset="utf-8">
<title>Granite Haulers Guild — Membership</title>
<link href="https://fonts.googleapis.com/css2?family=Rye&family=Open+Sans:ital,wght@0,700;0,800;1,700;1,800&family=Playfair+Display:wght@900&display=swap" rel="stylesheet">
<style>
  :root {
    --band-yellow: #e3d61a;
    --band-sage: #b4bda4;
    --title-gold: #8d6a22;
    --ink: #262626;
    --premier-red: #d42422;
    --seal-red: #c8141c;
    --exec-blue: #1f3f9c;
    --basic-gold: #e6cc12;
    --sky-top: #c9d6e1;
    --sky-mid: #e4ebf0;
    --field: #8fa46a;
    --road: #8d8d8a;
    --slogan: rgba(140, 98, 52, 0.55);
  }
  * { box-sizing: border-box; margin: 0; padding: 0; }
  html, body { width: 927px; height: 1200px; overflow: hidden; background: #fff; }
  .sheet {
    position: relative; width: 927px; height: 1200px; overflow: hidden;
    font-family: "Open Sans", Arial, sans-serif; color: var(--ink);
  }
  .scene {
    position: absolute; inset: 0;
    background: linear-gradient(180deg, var(--sky-top) 0%, var(--sky-mid) 40%, #eef1ee 58%, var(--field) 70%, #a8ab9c 78%, var(--road) 100%);
  }
  .scene-subject {
    position: absolute; left: 0; top: 480px; width: 640px; height: 720px;
    background: radial-gradient(ellipse 60% 45% at 50% 55%, #c41e22 0%, #b8343a 45%, rgba(160,70,70,0.5) 70%, rgba(140,140,140,0) 100%);
  }
  .title-band {
    position: absolute; left: 0; top: 0; width: 100%; height: 140px; background: var(--band-yellow);
  }
  .title {
    position: absolute; top: 36px; width: 100%; text-align: center;
    font-family: "Rye", serif; font-size: 56px; color: var(--title-gold); letter-spacing: 2px;
  }
  .sage-band {
    position: absolute; left: 0; top: 140px; width: 100%; height: 54px; background: var(--band-sage); opacity: 0.75;
  }
  .seal {
    position: absolute; display: flex; align-items: center; justify-content: center;
    border-radius: 50%; color: #fff; font-family: "Playfair Display", serif; font-weight: 900;
  }
  .seal--premier {
    left: 47px; top: 109px; width: 200px; height: 102px; font-size: 40px;
    background: radial-gradient(circle at 40% 35%, #ee3a3a, var(--seal-red) 70%);
    box-shadow: 0 0 0 5px #e0242a, 0 4px 8px rgba(0,0,0,0.35);
  }
  .seal--exec {
    left: 447px; top: 680px; width: 88px; height: 54px; font-size: 22px;
    background: radial-gradient(circle at 40% 35%, #3c66d6, #1a3a9a 70%);
    box-shadow: 0 0 0 3px #2f56c4;
  }
  .seal--basic {
    left: 547px; top: 914px; width: 80px; height: 40px; font-size: 18px;
    background: radial-gradient(circle at 40% 35%, #f3e04a, #c8ae0c 70%);
    box-shadow: 0 0 0 3px #dcc41c;
  }
  .tier-name {
    position: absolute; font-style: italic; font-weight: 800; text-decoration: underline;
  }
  .tier-name--premier { left: 289px; top: 148px; font-size: 41px; color: var(--premier-red); text-decoration-thickness: 3px; }
  .tier-name--exec { left: 571px; top: 690px; font-size: 20px; color: var(--exec-blue); }
  .tier-name--basic { left: 640px; top: 922px; font-size: 20px; color: var(--basic-gold); text-shadow: 0 0 2px #4a4000; }
  .premier-copy { position: absolute; left: 0; top: 200px; font-size: 22px; font-weight: 700; line-height: 35.4px; }
  .premier-copy .line { position: absolute; white-space: nowrap; }
  .benefit { color: var(--premier-red); font-style: italic; }
  .divider { position: absolute; border-top: 3px dashed #333; }
  .divider--main { left: 287px; top: 657px; width: 567px; border-top-width: 3px; }
  .divider--sub { left: 627px; top: 932px; width: 213px; border-top-width: 2px; opacity: 0; }
  .exec-copy {
    position: absolute; left: 536px; top: 718px; width: 320px; text-align: center;
    font-size: 15.5px; font-weight: 700; line-height: 24px;
  }
  .exec-copy .benefit { color: var(--exec-blue); }
  .divider--exec { left: 627px; top: 910px; width: 213px; border-top: 2px dashed #333; }
  .basic-copy {
    position: absolute; left: 620px; top: 952px; width: 200px; text-align: center;
    font-size: 15.5px; font-weight: 700; line-height: 23px;
  }
  .org-mark {
    position: absolute; left: 640px; top: 1036px; display: flex; align-items: center; gap: 10px;
    font-size: 22px; font-weight: 800; color: #1b1b1b;
  }
  .org-mark .square { width: 26px; height: 26px; background: #1b1b1b; }
  .slogan {
    position: absolute; left: 58px; top: 1122px; font-family: "Rye", serif; font-size: 54px;
    color: var(--slogan); white-space: nowrap; letter-spacing: 1px;
  }
</style>
</head>
<body>
<div class="sheet">
  <div class="scene" role="img" aria-label="Photo of a country road under a pale sky with green fields"></div>
  <div class="scene-subject" role="img" aria-label="Photo of a woman waving beside a red hatchback with its hood open"></div>

  <div class="title-band"></div>
  <h1 class="title">MEMBERSHIP</h1>
  <div class="sage-band"></div>

  <div class="seal seal--premier">$1,000</div>
  <h2 class="tier-name tier-name--premier">Premier Membership</h2>

  <div class="premier-copy">
    <div class="line" style="left:257px;top:0">Includes all the benefits you get today plus:</div>
    <div class="line" style="left:89px;top:36px"><span class="benefit">Free Legal Consulting</span> – With this membership you can call a lawyer up</div>
    <div class="line" style="left:89px;top:71px">every time SRLB hit you with a fine or a threat and ask for advice.&nbsp; If you</div>
    <div class="line" style="left:89px;top:106px">need representation you get it at a discount.</div>
    <div class="line" style="left:89px;top:142px"><span class="benefit">Free IM Training</span> – As an owner your IM training is free.</div>
    <div class="line" style="left:89px;top:177px">Staffing Requirements – You tell us how many drivers you need and we will</div>
    <div class="line" style="left:89px;top:212px">help you find them. We have a list with over 300 people waiting for work.</div>
    <div class="line" style="left:89px;top:248px"><span class="benefit">“Annual Towers Get Away”</span> – Once a year we will find a resort that you and</div>
    <div class="line" style="left:89px;top:283px">your spouse can go to with other leaders in the industry.&nbsp; We’ll meet for a hr</div>
    <div class="line" style="left:131px;top:318px">and play for the weekend.&nbsp; Have fun and get a tax write off.</div>
    <div class="line" style="left:156px;top:354px"><span class="benefit">Quarterly Strategy Meetings</span> – We lock ourselves up in a room for a</div>
    <div class="line" style="left:177px;top:389px">day and plan the future of the industry.&nbsp; Work on Problems, write</div>
    <div class="line" style="left:219px;top:424px">laws, identify company needs.</div>
  </div>

  <div class="divider divider--main"></div>

  <div class="seal seal--exec">$500</div>
  <h2 class="tier-name tier-name--exec">Executive Membership</h2>
  <div class="exec-copy">
    Includes all you get today plus:<br>
    <span class="benefit">Free Legal Consulting</span> – With this<br>
    membership you can call a lawyer up<br>
    every time SRLB hit you with a fine or a<br>
    threat and ask for advice.&nbsp; If you need<br>
    representation you get it at a discount<br>
    <span class="benefit">IM Training for only $75</span> – That’s a 50%<br>
    savings for your IM training (Owner)
  </div>

  <div class="divider divider--exec"></div>

  <div class="seal seal--basic">$200</div>
  <h2 class="tier-name tier-name--basic">Basic Membership</h2>
  <div class="basic-copy">– All the great benefits<br>you get today.</div>

  <div class="org-mark"><span class="square"></span>Granite Haulers Guild</div>

  <div class="slogan">LET’S PICK EACH OTHER UP!</div>
</div>
</body>
</html>
```